Veterinary TPLO Surgery Flyer Design

Please use this flyer to make a professional-looking 1 page, double-sided client handout regarding TPLO.

You can visit our website at www.brackenfieldpetcare.com & www.northwoodsanimalsurgerygroup.com for additional logo information. The flyer should include all the text from the one provided.

Target Market(s)

Client communication to for referral surgery between sister veterinary clinics

Industry/Entity Type

Veterinary

Requirements
Must have
• The text included
Nice to have
• Nice to have the Cedar Hollow Avenue Animal CLinic & Dr. Pell Mobile vet logos incorporated.

```html
<!DOCTYPE html>
<html lang="en">
<head>
<meta charset="utf-8">
<title>TPLO Surgery Client Handout</title>
<link rel="stylesheet" href="https://fonts.googleapis.com/css2?family=Montserrat:wght@400;500;600;700;800&family=Dancing+Script:wght@600&display=swap">
<style>
:root{
  --green:#50794a;
  --green-dark:#3f6339;
  --sage:#dfe7d4;
  --sage-soft:#edf1e6;
  --charcoal:#3c3d40;
  --ink:#333;
  --muted:#5a5a5a;
  --white:#fff;
  --backdrop:#e8e8e8;
}
*{box-sizing:border-box;margin:0;padding:0}
html,body{width:724px;height:1200px;overflow:hidden}
body{background:var(--backdrop);font-family:"Montserrat",sans-serif;color:var(--ink);position:relative}
.page{position:absolute;left:136px;width:452px;height:584px;background:var(--white);overflow:hidden;box-shadow:0 4px 14px rgba(0,0,0,.18)}
.page--front{top:8px}
.page--back{top:604px}
.abs{position:absolute}

/* front */
.front-green{position:absolute;left:0;top:0}
.brand{left:17px;top:16px;display:flex;align-items:center;gap:6px;color:var(--white)}
.brand__mark{width:16px;height:16px;background:var(--white);opacity:.9}
.brand__name{font-size:11.5px;font-weight:600;line-height:1.1}
.partner{left:352px;top:14px;width:86px;text-align:center}
.partner__dot{width:34px;height:34px;border-radius:50%;background:var(--green);margin:0 auto 5px}
.partner__name{font-size:8px;font-weight:600;color:var(--green-dark);line-height:1.2}
.headline{left:17px;top:68px;color:var(--white)}
.headline__big{font-size:27px;font-weight:800;line-height:1.02;letter-spacing:.3px}
.headline__script{font-family:"Dancing Script",cursive;font-size:19px;font-weight:600;margin-left:4px}
.headline__name{font-size:17px;font-weight:800;margin-top:3px}
.about{left:17px;top:162px;width:245px;color:var(--white);font-size:7.3px;line-height:1.38}
.about h3{font-size:8px;font-weight:700}
.hex-photo{position:absolute}
.section-title{font-size:12.5px;font-weight:700;color:var(--green)}
.benefits{left:242px;top:292px;width:200px}
.benefit{display:flex;gap:7px;margin-top:7px}
.benefit__icon{flex:none;width:15px;height:15px;border-radius:50%;background:var(--sage);position:relative;margin-top:2px}
.benefit__icon::after{content:"";position:absolute;left:5px;top:5px;width:5px;height:5px;border-radius:50%;background:var(--green)}
.benefit h4{font-size:8px;font-weight:700;color:var(--green-dark)}
.benefit p{font-size:7.5px;line-height:1.3;color:var(--muted)}
.what{left:17px;top:354px;width:240px}
.what p{font-size:7.6px;line-height:1.38;color:var(--muted);margin-top:6px}
.figure{position:absolute;top:463px;width:80px;height:67px;border:2px solid var(--green)}
.figure--knee{left:17px;background:linear-gradient(135deg,#d9d6c6,#b9b7a6)}
.figure--xray{left:125px;background:linear-gradient(135deg,#2b2b2b,#8a8a8a)}
.why{left:252px;top:447px;width:176px;height:100px;background:var(--sage);border-radius:6px;text-align:center;padding:24px 10px 0}
.why__tag{position:absolute;left:17px;top:-6px;width:142px;background:var(--green);color:var(--white);font-size:6.6px;padding:2px 0 3px}
.why__tag b{display:block;font-size:8px;font-weight:700;color:var(--green-dark);background:var(--white);margin:-12px auto 2px;width:80px}
.why p{font-size:6.6px;line-height:1.45;color:var(--muted)}
.footbar{left:0;top:552px}
.footbar__url{left:20px;top:562px;color:var(--white);font-size:7.8px;font-weight:600;display:flex;align-items:center;gap:6px}

/* back */
.radio{left:17px;top:16px;width:420px}
.radio h2{font-size:12.8px;font-weight:700;color:var(--green)}
.radio p{font-size:8px;line-height:1.3;color:var(--muted);width:262px;margin-top:7px}
.process{left:0;top:126px;width:452px;height:218px;background:var(--sage);padding:14px 17px 0}
.process h2{font-size:13px;font-weight:700;color:var(--ink)}
.process ol{list-style:none;margin-top:5px}
.process li{font-size:7.5px;line-height:1.38;color:var(--ink);margin-bottom:2.5px}
.post{left:0;top:354px;width:452px;text-align:center}
.post h2{font-size:13px;font-weight:700;color:var(--green)}
.post__sub{font-size:7.8px;color:var(--muted);margin-top:2px}
.post__cols{display:flex;margin:10px 22px 0}
.post__col{flex:1;padding:0 14px}
.post__col+.post__col{border-left:1.5px solid var(--green)}
.post__col h3{font-size:10px;font-weight:700;color:var(--ink)}
.post__col p{font-size:7px;line-height:1.35;color:var(--muted);margin-top:3px}
.post__note{font-size:7.6px;line-height:1.3;color:var(--muted);margin:12px 44px 0}
.clinic-label{left:17px;top:477px;font-size:7.8px;font-weight:700;color:var(--green-dark)}
.contact-bar{left:0;top:491px;width:452px;height:46px;background:var(--green);color:var(--white)}
.mobile-bar{left:0;top:537px;width:452px;height:47px;background:var(--charcoal);color:var(--white)}
.contact{position:absolute;display:flex;align-items:center;gap:6px;font-size:7.4px;font-weight:600}
.contact svg{flex:none}
</style>
</head>
<body>

<section class="page page--front" aria-label="Handout front">
  <svg class="front-green" width="452" height="345" viewBox="0 0 452 345" aria-hidden="true">
    <path d="M0 0H343V88H452V198C360 238 250 262 0 342Z" fill="var(--green)"/>
  </svg>

  <div class="abs brand"><span class="brand__mark"></span><span class="brand__name">Cedar Hollow Avenue<br>Animal Clinic</span></div>
  <div class="abs partner"><div class="partner__dot"></div><div class="partner__name">Dr. Renata Pell</div></div>

  <div class="abs headline">
    <div class="headline__big">ADVANCED</div>
    <div class="headline__big">ORTHOPEDIC<span class="headline__script">Care by</span></div>
    <div class="headline__name">DR. RENATA PELL</div>
  </div>

  <div class="abs about">
    <h3>About Dr. Renata Pell</h3>
    <p>Dr. Renata Pell is a board-certified veterinary surgeon (Diplomate of the National College of Veterinary Surgeons) with over 18 years of experience in small animal surgery. A graduate of Great Lakes State University, she completed her surgical residency at Harborview School of Veterinary Medicine. Through her mobile practice, Fieldside Surgical Care, Dr. Pell now provides advanced surgical procedures—such as TPLO directly at local clinics.</p>
  </div>

  <svg class="hex-photo" style="left:265px;top:102px" width="166" height="158" viewBox="0 0 166 158" role="img" aria-label="Photo of a child hugging a golden doodle dog outdoors">
    <defs><linearGradient id="hexA" x1="0" y1="0" x2="1" y2="1"><stop offset="0" stop-color="#7c8a5e"/><stop offset=".6" stop-color="#c9a774"/><stop offset="1" stop-color="#8f7750"/></linearGradient></defs>
    <polygon points="42,3 124,3 163,79 124,155 42,155 3,79" fill="var(--charcoal)"/>
    <polygon points="46,10 120,10 155,79 120,148 46,148 11,79" fill="url(#hexA)"/>
  </svg>

  <div class="abs benefits">
    <h2 class="section-title">Benefits of TPLO Surgery</h2>
    <div class="benefit"><span class="benefit__icon"></span><div><h4>Enhanced Joint Stability:</h4><p>Restores natural biomechanics, reducing pain and improving mobility</p></div></div>
    <div class="benefit"><span class="benefit__icon"></span><div><h4>Faster Recovery:</h4><p>Many dogs return to normal activity faster compared to other surgical techniques.</p></div></div>
    <div class="benefit"><span class="benefit__icon"></span><div><h4>Proven Long-Term Success:</h4><p>TPLO is particularly effective in large and active breeds.</p></div></div>
  </div>

  <div class="abs what">
    <h2 class="section-title">What is TPLO Surgery?</h2>
    <p>Tibial Plateau Leveling Osteotomy (TPLO) is a surgical procedure that stabilizes the stifle (knee) joint following a cranial cruciate ligament (CCL) rupture a common orthopedic injury in dogs. The procedure involves altering the angle of the tibial plateau to eliminate abnormal joint motion, restoring stability and improving function.</p>
  </div>

  <div class="figure figure--knee" role="img" aria-label="Illustration of a canine knee joint with torn cruciate ligament"></div>
  <div class="figure figure--xray" role="img" aria-label="Post-operative TPLO radiographs with bone plate"></div>

  <div class="abs why">
    <div class="why__tag"><b>WHY CHOOSE</b>Cedar Hollow Avenue Animal Clinic?</div>
    <p>Partnering with Dr. Pell, Cedar Hollow Avenue Animal Clinic offers advanced orthopedic surgery on-site—eliminating the need for referrals or travel. This collaboration ensures your pet receives expert surgical care in a familiar, trusted environment.</p>
  </div>

  <svg class="abs footbar" width="452" height="32" viewBox="0 0 452 32" aria-hidden="true">
    <path d="M0 0H222C236 0 240 32 256 32H0Z" fill="var(--charcoal)"/>
  </svg>
  <div class="abs footbar__url">
    <svg width="9" height="9" viewBox="0 0 10 10" aria-hidden="true"><circle cx="5" cy="5" r="4.3" fill="none" stroke="#fff" stroke-width="1"/><ellipse cx="5" cy="5" rx="1.8" ry="4.3" fill="none" stroke="#fff" stroke-width=".8"/><line x1=".7" y1="5" x2="9.3" y2="5" stroke="#fff" stroke-width=".8"/></svg>
    www.northwoodsanimalsurgerygroup.com
  </div>
</section>

<section class="page page--back" aria-label="Handout back">
  <div class="abs radio">
    <h2>Diagnostic Radiographs vs. TPLO Planning Radiographs</h2>
    <p>While diagnostic radiographs may confirm a CCL tear, they are not sufficient for surgical planning. TPLO requires three advanced technique radiographic views with precise measurements, which must be performed under sedation to reduce discomfort and allow accurate positioning</p>
  </div>

  <svg class="hex-photo" style="left:261px;top:60px" width="86" height="82" viewBox="0 0 86 82" role="img" aria-label="Photo of a yellow labrador sitting in a wooded area">
    <polygon points="22,2 64,2 84,41 64,80 22,80 2,41" fill="var(--sage-soft)"/>
    <polygon points="24,6 62,6 80,41 62,76 24,76 6,41" fill="#a59a7c"/>
  </svg>
  <svg class="hex-photo" style="left:349px;top:60px" width="92" height="86" viewBox="0 0 92 86" role="img" aria-label="Photo of a golden retriever lying on green grass">
    <polygon points="23,2 69,2 90,43 69,84 23,84 2,43" fill="var(--green)"/>
    <polygon points="26,7 66,7 85,43 66,79 26,79 7,43" fill="#8fae5e"/>
  </svg>

  <div class="abs process">
    <h2>Expected Process</h2>
    <ol>
      <li><b>1. Diagnosis:</b> Your pet is diagnosed with stifle instability (CCL tear) by your veterinarian.</li>
      <li><b>2. Referral:</b> Your veterinarian contacts the surgical coordinator at Cedar Hollow Avenue Animal Clinic.</li>
      <li><b>3. Consultation:</b> The coordinator contacts you to schedule a 1-hour consultation to review the procedure, estimated costs, and available surgery dates.</li>
      <li><b>4. Planning Radiographs:</b> These specialized X-rays are typically taken during the consultation under light sedation.</li>
      <li><b>5. Surgical Review:</b> Dr. Pell reviews the radiographs and your pet's medical history to confirm candidacy for TPLO.</li>
      <li><b>6. Deposit:</b> A $3,500 deposit secures Dr. Pell's travel and surgery date. This is refundable if canceled at least 5 days prior to the scheduled procedure.</li>
      <li><b>7. Surgery Day:</b> Your pet is dropped off in the morning and surgery is performed the same day.</li>
      <li><b>8. Discharge:</b> You'll receive a post-surgery update and your pet will go home that evening.</li>
    </ol>
  </div>

  <div class="abs post">
    <h2>Post-Operative Care &amp; Follow-Up</h2>
    <p class="post__sub">Two follow-up appointments will be scheduled:</p>
    <div class="post__cols">
      <div class="post__col"><h3>4 Weeks Post-Op:</h3><p>Evaluate healing, refill medications, and address any questions.</p></div>
      <div class="post__col"><h3>8 Weeks Post-Op:</h3><p>Sedated radiographs will confirm proper healing of the surgical site and tibia.</p></div>
    </div>
    <p class="post__note">Dr. Pell will stay in direct contact with you during your pet's recovery using her custom mobile app, which allows for secure messaging and provides detailed post-operative instructions.</p>
  </div>

  <div class="abs clinic-label">CEDAR HOLLOW AVENUE ANIMAL CLINIC</div>
  <div class="abs contact-bar">
    <div class="contact" style="left:17px;top:9px"><svg width="9" height="9" viewBox="0 0 10 10" aria-hidden="true"><path d="M2 1l2 .3.6 2-1.2 1a6 6 0 0 0 2.6 2.6l1-1.2 2 .6.3 2-1.3 1C4.5 9.4.6 5.5 1 2.3Z" fill="#fff"/></svg>(555) 014-2290</div>
    <div class="contact" style="left:17px;top:27px"><svg width="8" height="10" viewBox="0 0 8 10" aria-hidden="true"><path d="M4 10S0 5.6 0 3.8a4 4 0 0 1 8 0C8 5.6 4 10 4 10Z" fill="#fff"/><circle cx="4" cy="3.8" r="1.4" fill="var(--green)"/></svg>2740 Cedar Hollow Avenue, Brookfield, MI 48000</div>
    <div class="contact" style="left:295px;top:9px"><svg width="10" height="7" viewBox="0 0 10 7" aria-hidden="true"><rect width="10" height="7" fill="#fff"/><path d="M0 0l5 4 5-4" fill="none" stroke="var(--green)" stroke-width=".9"/></svg>info@brackenfieldpetcare.com</div>
    <div class="contact" style="left:295px;top:27px"><svg width="9" height="9" viewBox="0 0 10 10" aria-hidden="true"><circle cx="5" cy="5" r="4.3" fill="none" stroke="#fff"/><ellipse cx="5" cy="5" rx="1.8" ry="4.3" fill="none" stroke="#fff" stroke-width=".8"/><line x1=".7" y1="5" x2="9.3" y2="5" stroke="#fff" stroke-width=".8"/></svg>www.brackenfieldpetcare.com</div>
  </div>
  <div class="abs mobile-bar">
    <div class="contact" style="left:17px;top:10px">Fieldside Surgical Care</div>
    <div class="contact" style="left:17px;top:23px"><svg width="9" height="9" viewBox="0 0 10 10" aria-hidden="true"><path d="M2 1l2 .3.6 2-1.2 1a6 6 0 0 0 2.6 2.6l1-1.2 2 .6.3 2-1.3 1C4.5 9.4.6 5.5 1 2.3Z" fill="#fff"/></svg>555-018-7734</div>
    <div class="contact" style="left:280px;top:23px"><svg width="10" height="7" viewBox="0 0 10 7" aria-hidden="true"><rect width="10" height="7" fill="#fff"/><path d="M0 0l5 4 5-4" fill="none" stroke="var(--charcoal)" stroke-width=".9"/></svg>drpell@fieldsidesurgical.com</div>
  </div>
</section>

</body>
</html>
```